Wealth Management Business Card

We are a professional services consulting firm that specializes in high net worth individuals over $25,000,000, executives C-suite and above, closely held businesses owners, family offices and highly compensated employees.

Our focus is on risk mitigation and tax efficient strategies. Our clients take their risk on themselves and have a proven track record generating wealth. Our directive is to preserve and protect the wealth they’ve already created.

Our company Harbridge Advisory is geared around five directives of asset protection:
1) Legal Structuring
2) Leverage & Financing
3) Risk Management - Asset Protection & Insurance, Trustee Work
4) Asset Management & Investing - Under www.qelvantcapital.com
5) Tax Efficient Strategies

Our Company Mark is a Pentagon with a key in the middle. A pentagon is the most efficient defensive structure. Each point of a pentagon is equal distance front every point . Each side provides support to another and works together, which is the key to our clients success.

Our key colors are blue, black and silver.

We ‘re located in the Pacific Northwest with bi coastal and international clients. We have fewer, higher net worth clients and provide exceptional customer service. We do not do social media.

website is www.harbridgepath.com

Target Market(s)

High End Clients

Contact Information for Business Card

extra thick

Font styles to use
Serif

Requirements
Must have
• Metalic foil for lettering.
Black Background on one side
White Background on the other
Horizontal Format Only
No Rounded corners
Not Marketing sales information on the card.
Nice to have
• imprinted texture on the card
Should not have
• lots of color

```html
<!DOCTYPE html>
<html lang="en">
<head>
<meta charset="utf-8">
<title>Harbridge Advisory — Business Card</title>
<link rel="stylesheet" href="https://fonts.googleapis.com/css2?family=Cinzel:wght@400;600;700&display=swap">
<style>
  :root {
    --backdrop: #d9d4cc;
    --card-black: #231f20;
    --card-white: #ffffff;
    --silver: #bdbdbd;
    --navy: #0f2a6b;
    --blue: #1e63b5;
    --cyan: #14aee8;
    --band-end: #1553b0;
  }
  * { margin: 0; padding: 0; box-sizing: border-box; }
  html, body { width: 1200px; height: 965px; overflow: hidden; }
  body {
    background: var(--backdrop);
    position: relative;
    font-family: "Cinzel", "Times New Roman", serif;
  }
  .card {
    position: absolute;
    left: 278px;
    width: 647px;
    height: 370px;
    box-shadow: 0 8px 18px rgba(0,0,0,0.28);
    overflow: hidden;
  }
  .card::after {
    content: "";
    position: absolute;
    left: 0; right: 0; bottom: 0;
    height: 9px;
    background: linear-gradient(90deg, var(--cyan), var(--band-end));
  }
  .card--front { top: 97px; background: var(--card-black); }
  .card--back { top: 504px; background: var(--card-white); height: 368px; }

  .front-mark {
    position: absolute;
    left: 50%;
    top: 68px;
    width: 118px;
    height: 118px;
    margin-left: -59px;
    border-radius: 50%;
    background: var(--silver);
  }
  .front-name {
    position: absolute;
    left: 0; right: 0;
    top: 250px;
    text-align: center;
    color: var(--silver);
    font-weight: 700;
    font-size: 38px;
    letter-spacing: 1px;
  }

  .back-name {
    position: absolute;
    left: 22px;
    top: 44px;
    color: var(--navy);
    font-weight: 700;
    font-size: 25px;
    letter-spacing: 0.5px;
  }
  .person {
    position: absolute;
    left: 24px;
    top: 132px;
    color: var(--navy);
  }
  .person__name { font-size: 25px; font-weight: 700; line-height: 1.1; }
  .person__title { font-size: 16.5px; font-weight: 400; letter-spacing: 0.6px; }
  .divider {
    position: absolute;
    left: 24px;
    width: 232px;
    height: 1px;
    background: var(--blue);
  }
  .divider--one { top: 196px; }
  .divider--two { top: 260px; }
  .address {
    position: absolute;
    left: 24px;
    top: 206px;
    color: var(--navy);
    font-size: 16px;
    line-height: 22px;
    letter-spacing: 0.4px;
  }
  .contacts {
    position: absolute;
    left: 24px;
    top: 276px;
    list-style: none;
    color: var(--navy);
    font-size: 15px;
    line-height: 22px;
    letter-spacing: 0.3px;
  }
  .contacts li { display: flex; align-items: center; gap: 6px; }
  .contacts svg { width: 16px; height: 16px; flex: none; }
  .back-mark {
    position: absolute;
    left: 432px;
    top: 88px;
    width: 210px;
    height: 210px;
    border-radius: 50%;
    background: var(--navy);
  }
</style>
</head>
<body>
  <section class="card card--front">
    <div class="front-mark"></div>
    <div class="front-name">HARBRIDGE ADVISORY</div>
  </section>

  <section class="card card--back">
    <div class="back-name">HARBRIDGE ADVISORY</div>
    <div class="person">
      <div class="person__name">CORWIN ASHCOMBE</div>
      <div class="person__title">Founder &amp; Financial Strategist</div>
    </div>
    <div class="divider divider--one"></div>
    <div class="address">1420 Meridian Ave, Suite 304,<br>Cedar Hollow, OR 97108</div>
    <div class="divider divider--two"></div>
    <ul class="contacts">
      <li>
        <svg viewBox="0 0 16 16" aria-hidden="true"><path fill="#1e63b5" d="M3.5 1.5l2.5 0 1 3.5-1.7 1.2a8 8 0 0 0 4.5 4.5L11 9l3.5 1v2.5c0 1-1 2-2 2C6.5 14.5 1.5 9.5 1.5 3.5c0-1 1-2 2-2z"/></svg>
        (555) 014-2270
      </li>
      <li>
        <svg viewBox="0 0 16 16" aria-hidden="true"><rect x="1" y="3" width="14" height="10" fill="#1e63b5"/><path d="M1 3l7 6 7-6" fill="none" stroke="#fff" stroke-width="1.2"/></svg>
        INFO@HARBRIDGEPATH.COM
      </li>
      <li>
        <svg viewBox="0 0 16 16" aria-hidden="true"><circle cx="8" cy="8" r="7" fill="#1e63b5"/><path d="M1 8h14M8 1c-3 3-3 11 0 14M8 1c3 3 3 11 0 14" fill="none" stroke="#fff" stroke-width="0.9"/></svg>
        WWW.HARBRIDGEPATH.COM
      </li>
    </ul>
    <div class="back-mark"></div>
  </section>
</body>
</html>
```